Flyer für Reifen- und Autoservicebetrieb
Zielgruppe
Wir sind ein Reifen- und Autoservicebetrieb; eine freie KFZ-Meister-Werkstatt ohne Markenbindung.
Aufgabenstellung
Im Focus des Flyers soll auf der Vorderseite der Reifenservice stehen, da dieser zur bevorstehenden Winterreifen-Wechselsaison erscheinen wird (Reifenwechsel, Einlagerung, Räderwäsche, Online-Termin). Auf der Rückseite soll der Autoservice und der 'neu' angebotene LKW- und Landwirtschafts- Reifenservice beworben werden.

```html
<!DOCTYPE html>
<html lang="de">
<head>
<meta charset="utf-8">
<title>Korval Reifen – Flyer</title>
<link rel="stylesheet" href="https://fonts.googleapis.com/css2?family=Ubuntu:wght@400;500;700&family=Oswald:wght@300;400&family=Varela+Round&display=swap">
<style>
:root{
  --stage:#575757;
  --white:#ffffff;
  --ink:#1c1c1c;
  --orange:#f2a20c;
  --grey-band:#9a9a9a;
  --grey-mid:#8c8c8c;
  --tan:#b3945a;
  --snow-a:#eef3f8;
  --snow-b:#c9d5e2;
  --shop-a:#3b4656;
  --shop-b:#9aa5b2;
}
*{margin:0;padding:0;box-sizing:border-box}
html,body{width:1200px;height:830px;overflow:hidden;background:var(--stage)}
.page{position:absolute;top:11px;width:573px;height:808px;background:var(--white);overflow:hidden}
.front{left:13px;font-family:"Ubuntu",sans-serif;color:var(--ink)}
.back{left:616px;font-family:"Varela Round",sans-serif;color:var(--ink)}
.abs{position:absolute}

/* front */
.hero-photo{left:0;top:0;width:573px;height:282px;background:linear-gradient(180deg,var(--snow-a),var(--snow-b) 70%,#e9eef4)}
.hero-curve{left:0;top:250px;width:573px;height:40px}
.brand{font-family:"Ubuntu",sans-serif;font-weight:500;color:var(--orange);line-height:1}
.brand .sub{display:block;font-size:.42em;letter-spacing:.18em;margin-top:4px}
.front .brand{left:390px;top:124px;font-size:22px;display:flex;align-items:center;gap:8px}
.dot{width:12px;height:12px;border-radius:50%;background:var(--orange)}
.headline{left:0;width:573px;top:322px;text-align:center;font-size:32px;font-weight:700}
.services{left:22px;top:386px;width:540px;display:flex;justify-content:space-between}
.service{width:134px;text-align:center}
.service svg{display:block;margin:0 auto 10px;width:100px;height:90px}
.service h3{font-size:17px;font-weight:700;line-height:1.1}
.service p{font-size:12px;line-height:1.2;margin-top:2px}
.cta{left:101px;top:592px;width:372px;height:46px;border-radius:23px;background:var(--orange);color:var(--white);font-size:24px;font-weight:700;text-align:center;line-height:46px}
.phone{left:0;width:573px;top:665px;display:flex;justify-content:center;align-items:center;gap:14px;font-size:31px;font-weight:500}
.web{left:0;width:573px;top:708px;text-align:center;font-size:20px}
.front-footer{left:0;top:746px;width:573px;height:62px;background:var(--grey-band);color:var(--white);font-family:"Oswald",sans-serif;font-weight:300;font-size:17px;display:flex;align-items:center;justify-content:center;gap:18px}

/* back */
.shop-photo{left:0;top:0;width:573px;height:290px}
.back-title{left:24px;top:212px;font-family:"Oswald",sans-serif;font-size:37px;color:var(--ink);line-height:1}
.back-sub{left:183px;top:262px;font-family:"Oswald",sans-serif;font-size:37px;color:var(--orange);line-height:1}
.checklist{left:24px;top:322px;list-style:none;font-size:21.5px;line-height:26.3px}
.checklist li::before{content:"• "}
.back .brand{left:340px;top:388px;font-size:26px;display:flex;align-items:center;gap:10px}
.news-band{left:0;top:494px;width:573px;height:180px}
.news-title{left:24px;top:508px;font-family:"Ubuntu",sans-serif;font-weight:700;font-size:39px;color:var(--white)}
.news-text{left:24px;top:571px;font-size:17px;line-height:21px;color:var(--white);width:270px}
.vehicles{left:290px;top:512px;width:272px;height:150px;border-radius:6px;background:linear-gradient(90deg,#e0b23a,#3f8a2a)}
.back-cta{left:25px;top:716px;width:521px;height:36px;border:2px solid var(--orange);border-radius:18px;display:flex;overflow:hidden}
.back-cta .book{width:272px;background:var(--orange);color:var(--white);font-family:"Ubuntu",sans-serif;font-weight:700;font-size:17px;display:flex;align-items:center;justify-content:center;border-radius:0 18px 18px 0}
.back-cta .call{flex:1;display:flex;align-items:center;justify-content:center;gap:8px;font-family:"Ubuntu",sans-serif;font-weight:500;font-size:23px}
.back-footer{left:0;width:573px;top:766px;text-align:center;font-family:"Oswald",sans-serif;font-size:11.5px;word-spacing:1px}
</style>
</head>
<body>

<section class="page front">
  <div class="abs hero-photo" role="img" aria-label="Winterreifen stehen im Schnee bei fallenden Flocken"></div>
  <svg class="abs hero-curve" viewBox="0 0 573 40" preserveAspectRatio="none">
    <path d="M0 32 Q286 8 573 32 L573 40 L0 40Z" fill="var(--white)"/>
    <path d="M0 30 Q286 -2 573 30 Q286 12 0 30Z" fill="var(--orange)"/>
  </svg>
  <div class="abs brand"><span class="dot"></span><span>KORVAL REIFEN<span class="sub">UND AUTOSERVICE</span></span></div>

  <h1 class="abs headline">Bereit für den Winter?</h1>

  <div class="abs services">
    <div class="service">
      <svg viewBox="0 0 100 90"><path d="M30 5 H70 M95 45 L78 80 M5 45 L22 10 M30 85 H70" stroke="var(--orange)" stroke-width="2.5" fill="none"/>
        <ellipse cx="50" cy="45" rx="24" ry="30" fill="none" stroke="var(--ink)" stroke-width="5"/><ellipse cx="55" cy="45" rx="14" ry="22" fill="none" stroke="var(--ink)" stroke-width="4"/></svg>
      <h3>Reifenwechsel</h3><p>Professioneller<br>und schneller Service</p>
    </div>
    <div class="service">
      <svg viewBox="0 0 100 90"><path d="M30 5 H70 M95 45 L78 80 M5 45 L22 10 M30 85 H70" stroke="var(--orange)" stroke-width="2.5" fill="none"/>
        <g fill="none" stroke="var(--ink)" stroke-width="3"><rect x="28" y="22" width="34" height="10" rx="4"/><rect x="28" y="35" width="34" height="10" rx="4"/><rect x="28" y="48" width="34" height="10" rx="4"/><rect x="28" y="61" width="34" height="10" rx="4"/><circle cx="62" cy="58" r="14" fill="var(--white)"/><circle cx="62" cy="58" r="5"/></g></svg>
      <h3>Einlagerung</h3><p>Sicher und trocken<br>bis zur nächsten Saison</p>
    </div>
    <div class="service">
      <svg viewBox="0 0 100 90"><path d="M30 5 H70 M95 45 L78 80 M5 45 L22 10 M30 85 H70" stroke="var(--orange)" stroke-width="2.5" fill="none"/>
        <g fill="none" stroke="var(--ink)" stroke-width="3"><circle cx="52" cy="46" r="20"/><circle cx="52" cy="46" r="12"/><circle cx="52" cy="46" r="3"/><circle cx="72" cy="26" r="4"/><circle cx="30" cy="38" r="3"/><path d="M22 70 a7 7 0 0 1 10 -6 a8 8 0 0 1 14 4 H22Z"/></g></svg>
      <h3>Räderwäsche</h3><p>Glanz und Pflege<br>für Ihre Felgen</p>
    </div>
    <div class="service">
      <svg viewBox="0 0 100 90"><path d="M30 5 H70 M95 45 L78 80 M5 45 L22 10 M30 85 H70" stroke="var(--orange)" stroke-width="2.5" fill="none"/>
        <g fill="none" stroke="var(--ink)" stroke-width="3"><rect x="28" y="24" width="44" height="32" rx="2"/><path d="M45 56 V64 M38 66 H62"/><circle cx="48" cy="38" r="10"/><path d="M38 38 H58 M48 28 V48"/><path d="M58 42 L66 52 L62 53 Z" fill="var(--ink)"/></g></svg>
      <h3>Online-Termin</h3><p>Einfach<br>und bequem buchen</p>
    </div>
  </div>

  <div class="abs cta">Jetzt Termin online buchen!</div>
  <div class="abs phone">
    <svg width="28" height="28" viewBox="0 0 24 24"><path d="M6.6 10.8a15 15 0 0 0 6.6 6.6l2.2-2.2a1 1 0 0 1 1-.25 11.4 11.4 0 0 0 3.6.57 1 1 0 0 1 1 1V20a1 1 0 0 1-1 1A17 17 0 0 1 3 4a1 1 0 0 1 1-1h3.5a1 1 0 0 1 1 1c0 1.25.2 2.45.57 3.57a1 1 0 0 1-.25 1z" fill="var(--orange)"/></svg>
    <span>04531 987 65 43</span>
  </div>
  <p class="abs web">www.korval-reifen.de &nbsp;|&nbsp; Instagram: @korvalreifen</p>
  <div class="abs front-footer"><span>Sicher durch den Winter!</span><span>|</span><span>Service, der bewegt.</span><span>|</span><span>Reifen? Wir kümmern uns.</span></div>
</section>

<section class="page back">
  <svg class="abs shop-photo" viewBox="0 0 573 290" role="img" aria-label="Werkstatthalle mit Hebebühne, Autos und Werkzeug">
    <defs><linearGradient id="shop" x1="0" y1="0" x2="0" y2="1"><stop offset="0" stop-color="var(--shop-b)"/><stop offset="1" stop-color="var(--shop-a)"/></linearGradient></defs>
    <polygon points="0,0 573,0 573,279 0,183" fill="url(#shop)"/>
  </svg>
  <h2 class="abs back-title">Ihr Allround-Service –</h2>
  <p class="abs back-sub">jetzt auch für LKWs!</p>
  <ul class="abs checklist">
    <li>Ölwechsel &amp; Inspektion</li>
    <li>Bremsenservice</li>
    <li>TÜV-Vorbereitung</li>
    <li>Batterie-Check</li>
    <li>Klimaservice</li>
  </ul>
  <div class="abs brand"><span class="dot"></span><span>KORVAL REIFEN<span class="sub">UND AUTOSERVICE</span></span></div>

  <svg class="abs news-band" viewBox="0 0 573 180" preserveAspectRatio="none">
    <defs><linearGradient id="band" x1="0" x2="1"><stop offset="0" stop-color="var(--tan)"/><stop offset=".6" stop-color="#a29c90"/><stop offset="1" stop-color="var(--grey-band)"/></linearGradient></defs>
    <polygon points="0,0 227,0 268,80 0,80" fill="var(--grey-mid)"/>
    <rect x="0" y="80" width="573" height="100" fill="url(#band)"/>
    <polygon points="0,78 268,78 268,82 0,82" fill="var(--grey-mid)"/>
  </svg>
  <div class="abs news-title">Neu:</div>
  <p class="abs news-text">Reifenservice für Lastwagen und landwirtschaftliche Maschinen.</p>
  <div class="abs vehicles" role="img" aria-label="Gelber Lastwagen und grüner Traktor"></div>

  <div class="abs back-cta">
    <div class="book">Jetzt Termin online buchen!</div>
    <div class="call">
      <svg width="20" height="20" viewBox="0 0 24 24"><path d="M6.6 10.8a15 15 0 0 0 6.6 6.6l2.2-2.2a1 1 0 0 1 1-.25 11.4 11.4 0 0 0 3.6.57 1 1 0 0 1 1 1V20a1 1 0 0 1-1 1A17 17 0 0 1 3 4a1 1 0 0 1 1-1h3.5a1 1 0 0 1 1 1c0 1.25.2 2.45.57 3.57a1 1 0 0 1-.25 1z" fill="var(--orange)"/></svg>
      <span>04531 987 65 43</span>
    </div>
  </div>
  <p class="abs back-footer">Kompetenz auf allen Rädern. &nbsp; | &nbsp; Von PKW bis LKW – wir sind für Sie da. &nbsp; | &nbsp; Schnell. Sauber. Zuverlässig.</p>
</section>

</body>
</html>
```